Copper lark buildworks

Copper lark buildworks is a small construction company.
Who is a licenced builder, Carpenter, joiner,
working on heritage ,new build, speacial projects and sometimes furniture

Industry/Entity Type

Construction

```html
<!DOCTYPE html>
<html lang="en">
<head>
<meta charset="utf-8">
<title>Copper lark buildworks – Business Card</title>
<link rel="stylesheet" href="https://fonts.googleapis.com/css2?family=Oswald:wght@400&family=Roboto:wght@400&display=swap">
<style>
  :root {
    --page-bg: #e9e9e9;
    --card-bg: #ffffff;
    --brand-green: #5cb860;
    --pill-green-light: #63b865;
    --pill-green-dark: #2f8f3c;
    --icon-grey: #8a8a8a;
    --divider-grey: #b5b5b5;
    --on-green: #ffffff;
  }
  * { box-sizing: border-box; margin: 0; padding: 0; }
  html, body {
    width: 1200px;
    height: 900px;
    overflow: hidden;
    background: var(--page-bg);
  }
  .canvas {
    position: relative;
    width: 1200px;
    height: 900px;
  }
  .business-card {
    position: absolute;
    left: 150px;
    top: 193px;
    width: 900px;
    height: 514px;
    background: var(--card-bg);
    border-radius: 22px;
    box-shadow: 0 10px 30px rgba(0, 0, 0, 0.12);
  }
  .company-name {
    position: absolute;
    top: 118px;
    left: 0;
    right: 0;
    text-align: center;
    font-family: "Oswald", sans-serif;
    font-weight: 400;
    font-size: 74px;
    letter-spacing: -0.5px;
    color: var(--brand-green);
  }
  .contact-row {
    position: absolute;
    left: 96px;
    top: 360px;
    display: flex;
    align-items: center;
    gap: 28px;
  }
  .person-name {
    font-family: "Oswald", sans-serif;
    font-weight: 400;
    font-size: 58px;
    letter-spacing: -0.5px;
    color: var(--brand-green);
    line-height: 1;
  }
  .divider {
    width: 3px;
    height: 54px;
    background: var(--divider-grey);
    transform: skewX(-14deg);
  }
  .phone {
    display: flex;
    align-items: center;
    position: relative;
  }
  .phone-icon {
    width: 48px;
    height: 56px;
    position: relative;
    z-index: 1;
  }
  .phone-pill {
    margin-left: -14px;
    height: 58px;
    padding: 0 24px 0 44px;
    display: flex;
    align-items: center;
    border-radius: 0 8px 8px 0;
    background: linear-gradient(90deg, var(--pill-green-light), var(--pill-green-dark));
    font-family: "Roboto", sans-serif;
    font-weight: 400;
    font-size: 32px;
    letter-spacing: 1px;
    color: var(--on-green);
  }
</style>
</head>
<body>
<main class="canvas">
  <section class="business-card">
    <h1 class="company-name">Copper lark buildworks</h1>
    <div class="contact-row">
      <p class="person-name">Hollis Marrow</p>
      <span class="divider" aria-hidden="true"></span>
      <div class="phone">
        <svg class="phone-icon" viewBox="0 0 48 56" aria-hidden="true">
          <path fill="var(--icon-grey)" d="M14 4 L22 4 L24 16 L18 20 C18 30 22 38 30 42 L36 37 L46 42 L44 52 C28 54 6 38 8 10 Z"/>
        </svg>
        <span class="phone-pill">555 018 2746</span>
      </div>
    </div>
  </section>
</main>
</body>
</html>
```